Cooler Trailer Rental Flyer

I need a flyer designed to showcase a rental product.

We own two refrigerated Chill Haulers. One trailer is 7’ x 12’. The second trailer is 7’ x 16’. Each unit is a double axle trailer with a cargo capacity of 8000 lbs. The refrigeration unit is 110v and is capable of cooling or freezing with just 12 amps. The 12’ unit comes with a securely mounted generator for stand-alone service needs, and we have a portable generator available if needed for the 16’ unit.

The trailer requires a class III or class IV hitch, with a 2 5/16” ball for towing and a 7-pin two vehicle socket for the trailer wiring.

We offer delivery for $1.40 per loaded mile (we only charge for the miles with the trailer attached, so one way for delivery or pickup). This option may make sense for many reasons, including:
- saving the cost of your time
- saving the cost of fuel
- eliminating your liability for the trailer while towing
- preventing you from having to buy any towing equipment

Our farm is located at 4127 Tamsen Mill Avenue, Byron Center, Michigan 49315. The name of the farm/business is Maple Hollow Farm.

The rental rates are as follows:
$169/day (two day minimum rental required)
$599/week
$1500/month

A $100 deposit is required to reserve the trailer. The deposit is fully refundable up to two weeks prior to the event, 50% up to one week, and non-refundable within one week of the event.

The website for the place we bought the trailer is www.frostvanhaul.example. A link to a video from his website is https://frostvanhaul.example/refrigerated-trailer-videos/

I would like the flyer to be colorful and professional, with photos.
Updates

Several notes: 1. I have added the logo for Maple Hollow Farm. 2. Contact information for the brochure should be as follows: Martin or Rebecca Kowalder Maple Hollow Farm 1874 Maple Hollow Lane SW Byron Center, MI 49315 (555) 014-7290 3. Please note that we are not "FrostVanHaul.example". This is the website for the manufacturer of the trailers.

Here are some rental ideas that might be worth including: Emergencies and Power Outages Food Distributors Food Vendors Restaurants Caterers Ice Vendors Pubs and Microbreweries Resorts Festivals Open Markets Sporting Events Parties Weddings Floral Distributors Meat Processors Hunters

e-mail address is maplehollowfarm@mailbox.example

Target Market(s)

Food distributors, caterers, resorts, events (festivals, weddings, fairs, parades, parties, concerts), restaurants, breweries, farmers markets, vending companies, big game hunters

Font styles to use
Serif
Sans Serif

Colors

Designer to choose colors to be used in the design.

Requirements
Nice to have
• Tri-fold flyer

```html
<!DOCTYPE html>
<html lang="en">
<head>
<meta charset="UTF-8">
<title>Chill Haulers Rental – Tri-fold Inside</title>
<link href="https://fonts.googleapis.com/css2?family=Playfair+Display:ital,wght@0,700;0,800;1,400;1,500&family=Poppins:wght@400;500;600;700&display=swap" rel="stylesheet">
<style>
  :root{
    --navy:#2b3378;
    --navy-deep:#1d2360;
    --navy-soft:#3d4690;
    --orange:#f29a1f;
    --orange-deep:#e9861a;
    --gold:#f2b12e;
    --white:#ffffff;
    --ink:#4a4a5a;
    --rate-box:#e9e9ee;
    --page:#e8e6e1;
  }
  *{box-sizing:border-box;margin:0;padding:0}
  html,body{width:1200px;height:900px;overflow:hidden;background:var(--page)}
  body{font-family:"Poppins",sans-serif;color:var(--ink)}
  .brochure{position:absolute;left:30px;top:50px;width:1140px;height:800px;display:flex;box-shadow:0 10px 30px rgba(0,0,0,.18)}
  .panel{position:relative;width:380px;height:800px;overflow:hidden}
  .panel svg.art{position:absolute;inset:0;width:100%;height:100%}

  /* left panel */
  .panel--intro{background:var(--white)}
  .intro__copy{position:absolute;left:38px;top:70px;width:310px}
  .eyebrow{font-family:"Poppins",sans-serif;color:var(--orange);font-size:17px;font-weight:500;line-height:1}
  .intro__title{font-family:"Playfair Display",serif;font-weight:800;color:var(--navy);font-size:27px;line-height:1.1;margin-top:4px}
  .intro__sizes{border-left:3px solid var(--orange);padding-left:12px;margin-top:18px;font-weight:600;font-size:16px;line-height:1.35;color:#3a3a48}
  .intro__note{margin-top:14px;font-size:11.5px;line-height:1.5;color:var(--ink)}
  .hl{color:var(--orange);font-weight:700}

  /* middle panel */
  .panel--details{background:linear-gradient(160deg,var(--navy-soft),var(--navy) 55%,var(--navy-deep))}
  .details__copy{position:absolute;left:34px;top:56px;width:316px;color:var(--white)}
  .lead{font-family:"Playfair Display",serif;font-style:italic;color:var(--gold);font-size:15px;line-height:1.45}
  .specs{list-style:none;margin-top:26px}
  .specs li{position:relative;padding-left:22px;font-size:12px;line-height:1.5;margin-bottom:16px}
  .specs li::before{content:"";position:absolute;left:0;top:5px;width:9px;height:9px;background:var(--gold)}
  .specs .hl{color:var(--gold)}
  .reasons__title{font-family:"Playfair Display",serif;font-style:italic;color:var(--gold);font-size:16px;line-height:1.35;margin-top:22px}
  .reasons{list-style:none;margin-top:18px}
  .reasons li{display:flex;align-items:center;gap:14px;margin-bottom:12px;font-size:12.5px;line-height:1.35}
  .reasons .icon{flex:0 0 36px;height:36px;background:var(--orange);display:flex;align-items:center;justify-content:center}
  .reasons .icon svg{width:22px;height:22px}

  /* right panel */
  .panel--pricing{background:var(--white)}
  .pricing__copy{position:absolute;left:36px;top:62px;width:290px}
  .pricing__title{font-family:"Playfair Display",serif;font-weight:800;color:var(--navy);font-size:27px;line-height:1.1;margin-top:4px}
  .pricing__text{margin-top:12px;font-size:11.5px;line-height:1.5}
  .rates__title{font-family:"Playfair Display",serif;font-weight:700;color:var(--navy);font-size:14px;margin-top:16px}
  .rates{list-style:none;margin-top:14px}
  .rate{display:flex;align-items:stretch;height:46px;margin-bottom:12px}
  .rate__num{width:46px;background:var(--navy);color:var(--white);font-family:"Playfair Display",serif;font-weight:700;font-size:20px;display:flex;align-items:center;justify-content:center}
  .rate__box{flex:1;background:var(--rate-box);box-shadow:2px 3px 6px rgba(0,0,0,.15);display:flex;flex-direction:column;justify-content:center;padding-left:16px;font-weight:700;color:#2c2c38;font-size:15px;line-height:1.1}
  .rate__box small{font-weight:400;font-size:9px;color:var(--ink)}
</style>
</head>
<body>
<main class="brochure">

  <section class="panel panel--intro">
    <svg class="art" viewBox="0 0 380 800" preserveAspectRatio="none">
      <defs>
        <linearGradient id="trailerPhoto" x1="0" y1="0" x2="0" y2="1">
          <stop offset="0" stop-color="#a9c3e3"/>
          <stop offset=".45" stop-color="#e4e8ec"/>
          <stop offset="1" stop-color="#8d8f92"/>
        </linearGradient>
      </defs>
      <polygon points="0,432 380,500 380,800 0,800" fill="url(#trailerPhoto)" role="img" aria-label="Photo of a white refrigerated double-axle trailer with a roof-mounted cooling unit"/>
      <polygon points="0,392 380,462 380,500 0,432" fill="var(--orange)"/>
      <polygon points="305,360 380,300 380,462 322,451" fill="var(--navy)"/>
      <polygon points="232,352 336,352 290,420" fill="var(--orange-deep)"/>
    </svg>
    <div class="intro__copy">
      <p class="eyebrow">We own</p>
      <h1 class="intro__title">two refrigerated<br>Chill Haulers.</h1>
      <p class="intro__sizes">One trailer is 7’ x 12’.<br>The second trailer is 7’ x 16’.</p>
      <p class="intro__note">Each unit is a double axle trailer with a cargo capacity of <span class="hl">8000 lbs.</span></p>
    </div>
  </section>

  <section class="panel panel--details">
    <svg class="art" viewBox="0 0 380 800" preserveAspectRatio="none">
      <rect x="0" y="0" width="380" height="330" fill="#56609a" opacity=".28" role="img" aria-label="Faint photo of a trailer parked under trees"/>
      <polygon points="0,690 70,800 0,800" fill="var(--white)"/>
    </svg>
    <div class="details__copy">
      <p class="lead">The refrigeration unit is 110v and is capable of cooling or freezing with just 12 amps. The 12’ unit comes with a securely mounted generator for stand-alone service needs, and we have a portable generator available if needed for the 16’ unit.</p>
      <ul class="specs">
        <li>The trailer requires a class III or class IV hitch, with a <span class="hl">2 5/16”</span> ball for towing and a <span class="hl">7-pin</span> two vehicle socket for the trailer wiring.</li>
        <li>We offer delivery for <span class="hl">$1.40</span> per loaded mile (we only charge for the miles with the trailer attached, so one way for delivery or pickup).</li>
      </ul>
      <p class="reasons__title">This option may make sense for many reasons, including:</p>
      <ul class="reasons">
        <li><span class="icon"><svg viewBox="0 0 24 24" fill="none" stroke="#fff" stroke-width="2"><circle cx="12" cy="12" r="9"/><path d="M12 7v5l3 2"/></svg></span>Saving the cost of your time</li>
        <li><span class="icon"><svg viewBox="0 0 24 24" fill="none" stroke="#fff" stroke-width="2"><rect x="5" y="4" width="9" height="16" rx="1"/><path d="M5 10h9M14 8l4 3v7a1.5 1.5 0 0 0 3 0V9"/></svg></span>Saving the cost of fuel</li>
        <li><span class="icon"><svg viewBox="0 0 24 24" fill="none" stroke="#fff" stroke-width="2"><rect x="2" y="7" width="14" height="9"/><path d="M16 10h4l2 3v3h-6"/><circle cx="6" cy="18" r="2"/><circle cx="18" cy="18" r="2"/></svg></span>Eliminating your liability for the trailer while towing</li>
        <li><span class="icon"><svg viewBox="0 0 24 24" fill="none" stroke="#fff" stroke-width="2"><circle cx="9" cy="14" r="3"/><path d="M12 14h8M16 14v4"/><path d="M4 4l16 16M20 4L4 20"/></svg></span>Preventing you from having to buy any towing equipment</li>
      </ul>
    </div>
  </section>

  <section class="panel panel--pricing">
    <svg class="art" viewBox="0 0 380 800" preserveAspectRatio="none">
      <polygon points="330,0 380,0 380,330 352,300" fill="var(--orange)"/>
      <polygon points="0,600 60,520 380,430 380,800 0,800" fill="var(--navy)"/>
      <polygon points="0,640 0,760 40,700" fill="var(--orange)"/>
      <polygon points="0,560 70,520 70,740 0,740" fill="var(--orange-deep)"/>
      <rect x="40" y="500" width="300" height="220" fill="var(--white)"/>
      <rect x="52" y="512" width="276" height="196" fill="#b8c6d6" role="img" aria-label="Photo of a refrigerated trailer parked on a gravel lot"/>
      <rect x="52" y="640" width="276" height="68" fill="#c7b8a0" opacity=".8"/>
    </svg>
    <div class="pricing__copy">
      <p class="eyebrow">Rental</p>
      <h2 class="pricing__title">Product Price</h2>
      <p class="pricing__text">A $100 deposit is required to reserve the trailer. The deposit is fully refundable up to two weeks prior to the event, 50% up to one week, and non-refundable within one week of the event.</p>
      <p class="rates__title">The rental rates are as follows:</p>
      <ol class="rates">
        <li class="rate"><span class="rate__num">1</span><span class="rate__box">$169/day<small>two day minimum rental required</small></span></li>
        <li class="rate"><span class="rate__num">2</span><span class="rate__box">$599/week</span></li>
        <li class="rate"><span class="rate__num">3</span><span class="rate__box">$1500/month</span></li>
      </ol>
    </div>
  </section>

</main>
</body>
</html>
```